Business Card Design

I need Business card designs with following on cards:

Dorian Felsk
Director

M: +61 491 208 356
D: +61 7 5580 1926
F: +61 7 5580 6471
E: dorian@mevrostrand.example.au

Mevro Group
Suite 4/61 North Calloway Road
Tindall Point QLD 4299

Ross Halvorn
Director

M: +61 438 902 615
D: +61 7 5580 1926
F: +61 7 5580 6471
E: ross@mevrostrand.example.au

Mevro Group
Tindall Point QLD 4299

Mevro Group Logo has been attached to brief.

Industry/Entity Type

Business

```html
<!DOCTYPE html>
<html lang="en">
<head>
<meta charset="utf-8">
<title>Mevro Group — Business Cards</title>
<link rel="stylesheet" href="https://fonts.googleapis.com/css2?family=Source+Sans+3:wght@300;400;600&display=swap">
<style>
  :root {
    --brand-blue: #0a64b4;
    --brand-blue-deep: #06428a;
    --brand-blue-light: #1f86d6;
    --ink: #2b2b2b;
    --ink-soft: #5a5a5a;
    --rule: #c9ced4;
    --card-white: #fbfbfb;
    --backdrop: #e9e7e3;
  }
  * { box-sizing: border-box; margin: 0; padding: 0; }
  html, body {
    width: 1200px; height: 1024px; overflow: hidden;
    background: var(--backdrop);
    font-family: "Source Sans 3", "Myriad Pro", sans-serif;
  }
  .sheet {
    width: 1200px; height: 1024px;
    display: flex; flex-direction: column;
    align-items: center; justify-content: center; gap: 48px;
  }
  .card {
    width: 770px; height: 440px; position: relative; overflow: hidden;
    box-shadow: 0 10px 28px rgba(0,0,0,.18);
  }

  /* Front */
  .card--front {
    background: radial-gradient(ellipse at 45% 40%, var(--brand-blue-light) 0%, var(--brand-blue) 55%, var(--brand-blue-deep) 100%);
    display: flex; flex-direction: column; align-items: center; justify-content: center;
  }
  .brand { display: flex; align-items: center; gap: 18px; }
  .brand__dot { border-radius: 50%; flex: none; }
  .brand__name { font-weight: 300; letter-spacing: .01em; line-height: 1; }
  .card--front .brand__dot { width: 56px; height: 56px; background: #fff; }
  .card--front .brand__name { color: #fff; font-size: 64px; }
  .front__url {
    position: absolute; bottom: 42px; left: 0; right: 0; text-align: center;
    color: #fff; font-size: 19px; font-weight: 300; letter-spacing: .32em;
  }

  /* Back */
  .card--back { background: var(--card-white); }
  .back__band { position: absolute; left: 0; right: 0; bottom: 0; height: 22px; background: var(--brand-blue); }
  .back__logo {
    position: absolute; left: 0; top: 0; width: 300px; height: 418px;
    display: flex; align-items: center; justify-content: center;
  }
  .card--back .brand { flex-direction: column; gap: 14px; }
  .card--back .brand__dot { width: 70px; height: 70px; background: var(--brand-blue); }
  .card--back .brand__name { color: var(--brand-blue); font-size: 44px; }
  .back__divider {
    position: absolute; left: 300px; top: 50px; bottom: 72px; width: 1px; background: var(--rule);
  }
  .back__details { position: absolute; left: 344px; top: 46px; right: 30px; }
  .person__name { color: var(--brand-blue); font-size: 36px; font-weight: 400; line-height: 1.05; }
  .person__role { color: var(--ink); font-size: 21px; font-weight: 400; margin-top: 2px; }
  .contact-list { list-style: none; margin-top: 22px; }
  .contact-list li {
    display: flex; align-items: center; gap: 14px;
    color: var(--ink); font-size: 18px; line-height: 1.55;
  }
  .icon { width: 16px; height: 16px; flex: none; fill: var(--brand-blue); }
  .address { display: flex; gap: 14px; margin-top: 18px; }
  .address .icon { margin-top: 4px; }
  .address__lines { font-size: 18px; line-height: 1.35; color: var(--ink); }
  .address__company { color: var(--brand-blue); }
</style>
</head>
<body>
<main class="sheet">

  <section class="card card--front" aria-label="Card front">
    <div class="brand">
      <span class="brand__dot"></span>
      <span class="brand__name">mevro group</span>
    </div>
    <p class="front__url">www.mevrostrand.example.au</p>
  </section>

  <section class="card card--back" aria-label="Card back">
    <div class="back__logo">
      <div class="brand">
        <span class="brand__dot"></span>
        <span class="brand__name">mevro group</span>
      </div>
    </div>
    <div class="back__divider"></div>

    <div class="back__details">
      <h1 class="person__name">Dorian Felsk</h1>
      <p class="person__role">Director</p>

      <ul class="contact-list">
        <li>
          <svg class="icon" viewBox="0 0 16 16" aria-hidden="true"><rect x="4" y="0.5" width="8" height="15" rx="1.5"/><rect x="5.5" y="2.5" width="5" height="9" fill="#fff"/></svg>
          +61 491 208 356
        </li>
        <li>
          <svg class="icon" viewBox="0 0 16 16" aria-hidden="true"><path d="M3.6 1 6 3.9 4.7 5.6c.9 2.3 2.8 4.2 5.1 5.1l1.7-1.3 2.9 2.4-1.5 2.6C7.4 14.2 1.8 8.6 1.2 2.9z"/></svg>
          +61 7 5580 1926
        </li>
        <li>
          <svg class="icon" viewBox="0 0 16 16" aria-hidden="true"><rect x="4" y="1" width="8" height="5"/><rect x="1" y="6" width="14" height="7" rx="1"/><rect x="4" y="11" width="8" height="4" fill="#fff" stroke="#0a64b4" stroke-width="1"/></svg>
          +61 7 5580 6471
        </li>
        <li>
          <svg class="icon" viewBox="0 0 16 16" aria-hidden="true"><rect x="1" y="3" width="14" height="10" rx="1"/><path d="M1.8 3.8 8 9l6.2-5.2" fill="none" stroke="#fff" stroke-width="1.3"/></svg>
          dorian@mevrostrand.example.au
        </li>
      </ul>

      <div class="address">
        <svg class="icon" viewBox="0 0 16 16" aria-hidden="true"><path d="M8 0.5a5 5 0 0 0-5 5c0 3.8 5 10 5 10s5-6.2 5-10a5 5 0 0 0-5-5zm0 7a2 2 0 1 1 0-4 2 2 0 0 1 0 4z"/></svg>
        <p class="address__lines">
          <span class="address__company">Mevro Group</span><br>
          Suite 4/61 North Calloway Road<br>
          Tindall Point QLD 4299
        </p>
      </div>
    </div>

    <div class="back__band"></div>
  </section>

</main>
</body>
</html>
```